Redesign of Current Wix Website - Event Production Company

Our website is www.trulvanshows.com and we need a redesign. We are full service event production company offering clients services including event management, graphics and content creation, vendor sourcing and management, contract review, audio visual production and venue selection. We would like our website to look more like an event management company, not just an audio visual company which it looks like now.
We want to look more like www.basquirelabs.com
Our Wix account is FILLED with logos, pictures and all the graphics you will need and we can assist with assets, categories and text.
On the Logo, I want to move away from "TRV Shows" and move to "Halvindor Stage Production" and I would like a redesigned logo with the same center element but a name change. I do have the art work files for the logo, vector and ai.

Target Market(s)

Event Planners and people that book event services. Assistants of CEOs. Marketing Directors. Gala Chairpersons and people in positions to purchase large scale event production

Industry/Entity Type

Event Management and Production - Corporate and Social

Coding

Coded - Design and coding required

Font styles to use
Other font styles liked:
• my logo is multicolor. look at it before you design

Colors
0054AA
0677BA
7BADD7
CADEEF
E8F1F8
6B429C
8869AF
B7A5CE
E3DAEB
F3F0F8

Requirements
Must have
• A clean professional look that shows the client who we are and what we do, and the full scope of what we do.
Nice to have
• www.basquirelabs.com ; https://themarbledrift.com/ look at these two website We are going after venues, planners end clients. Much like the on service page.

```html
<!DOCTYPE html>
<html lang="en">
<head>
<meta charset="utf-8">
<title>Halvindor Stage Production</title>
<link rel="stylesheet" href="https://fonts.googleapis.com/css2?family=Anton&family=Montserrat:wght@400;500;600;700&display=swap">
<style>
:root{
  --bg:#0c0c0f;
  --bg-soft:#121216;
  --purple:#6b429c;
  --purple-btn:#7a4fb3;
  --purple-deep:#3a1a5f;
  --card:#2a2136;
  --lavender:#b7a5ce;
  --blue:#0677ba;
  --blue-light:#7badd7;
  --text:#ffffff;
  --muted:#d6d6dc;
}
*{margin:0;padding:0;box-sizing:border-box}
html,body{width:1200px;height:4631px;overflow:hidden;background:var(--bg);color:var(--text);font-family:"Montserrat",sans-serif}
.page{position:relative;width:1200px;height:4631px}
.abs{position:absolute}
.display{font-family:"Anton",sans-serif;font-weight:400;letter-spacing:.5px;text-transform:none}
.btn{position:absolute;display:flex;align-items:center;justify-content:center;background:var(--purple-btn);color:#fff;font-weight:700;font-size:14px;letter-spacing:.3px;border-radius:5px;text-transform:uppercase}

/* header */
.site-header{position:absolute;left:0;top:0;width:1200px;height:110px;z-index:3}
.nav-link{position:absolute;top:47px;font-size:14px;color:#fff}
.brand{position:absolute;left:500px;top:20px;width:200px;height:72px;display:flex;flex-direction:column;align-items:center;justify-content:center;gap:6px}
.brand-dot{width:34px;height:34px;border-radius:50%;background:var(--purple)}
.brand-name{font-size:11px;font-weight:700;color:#fff;letter-spacing:.4px;text-transform:uppercase}
.phone{position:absolute;left:976px;top:39px;width:164px;height:34px;border:1px solid #fff;border-radius:3px;display:flex;align-items:center;justify-content:center;gap:6px;font-size:13px}

/* hero */
.hero{position:absolute;left:0;top:0;width:1200px;height:670px;background:linear-gradient(180deg,#0c0c10 0%,#3a2a48 18%,#5a4660 40%,#3b2a38 70%,#0c0c0f 100%)}
.hero-title{position:absolute;left:0;top:262px;width:1200px;text-align:center;font-size:76px;line-height:94px;color:#fff}
.social-rail{position:absolute;left:1148px;top:525px;width:52px;height:150px;background:var(--purple);display:flex;flex-direction:column;align-items:center;justify-content:center;gap:16px}
.social-rail span{width:22px;height:22px;border:2px solid #fff;border-radius:4px}

/* intro */
.intro-heading{position:absolute;left:60px;top:852px;width:520px;font-size:40px;font-weight:600;line-height:51px}
.intro-copy{position:absolute;left:629px;top:857px;width:450px;font-size:16px;line-height:27px;color:var(--muted)}

/* bands */
.photo-band{position:absolute;left:0;width:1200px}
.band-title{position:absolute;left:0;width:1200px;text-align:center;color:#fff}

/* features */
.feature-heading{position:absolute;font-size:40px;font-weight:600;line-height:51px}
.feature-list{position:absolute;list-style:none}
.feature-list li{position:relative;padding-left:52px;font-size:16px;line-height:27px;color:var(--muted);margin-bottom:34px}
.feature-list li b{color:#fff;font-weight:700}
.feature-list svg{position:absolute;left:0;top:9px}
.photo{position:absolute;border-radius:4px}

/* services */
.service-card{position:absolute;width:347px;height:345px;background:var(--card);border-radius:8px;text-align:center}
.service-card .thumb{position:absolute;left:22px;top:18px;width:303px;height:172px;border:1px solid #fff}
.service-card h3{position:absolute;left:15px;right:15px;top:206px;font-size:22px;font-weight:700;line-height:28px}
.service-card p{position:absolute;left:26px;right:26px;font-size:12px;line-height:16px;color:var(--muted)}

/* testimonial */
.quote-copy{position:absolute;left:105px;top:4035px;width:510px;font-size:18px;line-height:28px;color:#e6e6ea}
.quote-copy b{color:#fff}

/* cta */
.cta{position:absolute;left:0;top:4358px;width:1200px;height:182px;background:var(--purple-deep)}
.site-footer{position:absolute;left:0;top:4540px;width:1200px;height:91px;display:flex;align-items:center;justify-content:center;font-size:13px;color:var(--muted)}
</style>
</head>
<body>
<div class="page">

  <section class="hero">
    <div role="img" aria-label="Banquet hall with round dinner tables set for a gala under purple uplighting" style="position:absolute;inset:0"></div>
    <h1 class="hero-title display">Transform Your Vision Into<br>Unforgettable Moments</h1>
    <a class="btn" style="left:472px;top:507px;width:255px;height:48px">Request a Free Quote</a>
  </section>

  <header class="site-header">
    <a class="nav-link" style="left:60px">Event Production</a>
    <a class="nav-link" style="left:221px">Content Creation</a>
    <div class="brand"><span class="brand-dot"></span><span class="brand-name">Halvindor Stage Production</span></div>
    <a class="nav-link" style="left:851px">Social Media</a>
    <a class="phone"><svg width="14" height="14" viewBox="0 0 24 24"><path fill="#fff" d="M6.6 10.8a15.1 15.1 0 0 0 6.6 6.6l2.2-2.2a1 1 0 0 1 1-.25 11.4 11.4 0 0 0 3.6.57 1 1 0 0 1 1 1V20a1 1 0 0 1-1 1A17 17 0 0 1 3 4a1 1 0 0 1 1-1h3.5a1 1 0 0 1 1 1c0 1.25.2 2.45.57 3.6a1 1 0 0 1-.25 1z"/></svg>(888) 555-0147</a>
  </header>

  <nav class="social-rail" aria-label="Social media links"><span></span><span></span><span></span></nav>

  <section class="intro">
    <h2 class="intro-heading">Full-Service Event Production That Thrills, Inspires, and Exceeds Expectation</h2>
    <p class="intro-copy">At Halvindor Stage Productions, we're architects of awe. Whether you're commanding a crowd at a live event or captivating audiences through film, we blend technical mastery and creative storytelling to turn ideas into indelible moments.</p>
    <a class="btn" style="left:629px;top:1052px;width:184px;height:46px">View Services</a>
  </section>

  <section>
    <div class="photo-band" role="img" aria-label="Ballroom with chandeliers, speakers at a podium and projection screens" style="top:1240px;height:390px;background:linear-gradient(180deg,#2a2530 0%,#6e5c4c 35%,#5a4a3e 65%,#0c0c0f 100%)"></div>
    <h2 class="band-title display" style="top:1548px;font-size:74px;line-height:90px">WHY CHOOSE US?</h2>
  </section>

  <section>
    <h2 class="feature-heading" style="left:60px;top:1680px;width:560px">Event Production That Wows</h2>
    <ul class="feature-list" style="left:60px;top:1808px;width:560px">
      <li><svg width="32" height="32" viewBox="0 0 32 32"><rect width="32" height="32" rx="4" fill="var(--blue)"/><path d="M8 16l6 6 11-12" stroke="#fff" stroke-width="2.5" fill="none"/></svg><b>Immersive Experiences:</b> Lighting, staging, AV, and logistics that transform venues into worlds.</li>
      <li><svg width="32" height="32" viewBox="0 0 32 32"><rect width="32" height="32" rx="4" fill="var(--blue)"/><path d="M8 16l6 6 11-12" stroke="#fff" stroke-width="2.5" fill="none"/></svg><b>Strategic Planning:</b> Stress-free execution for corporate galas, weddings, product launches, and more.</li>
      <li><svg width="32" height="32" viewBox="0 0 32 32"><rect width="32" height="32" rx="4" fill="var(--blue)"/><path d="M8 16l6 6 11-12" stroke="#fff" stroke-width="2.5" fill="none"/></svg><b>Bespoke Design:</b> Spaces that mirror your brand's soul, down to the last detail.</li>
    </ul>
    <div class="photo" role="img" aria-label="Audio engineer at a mixing desk overlooking a full banquet room" style="left:673px;top:1683px;width:467px;height:392px;background:linear-gradient(160deg,#3b3658,#4a3e3a 55%,#1c1a20)"></div>

    <div class="photo" role="img" aria-label="Camera operator filming a gala from behind monitors and a tripod" style="left:60px;top:2162px;width:467px;height:393px;background:linear-gradient(160deg,#2c2e48,#54483e 55%,#1a1a1e)"></div>
    <h2 class="feature-heading" style="left:588px;top:2158px;width:560px">Film &amp; Content Creation That Resonates</h2>
    <ul class="feature-list" style="left:588px;top:2287px;width:552px">
      <li><svg width="32" height="32" viewBox="0 0 32 32"><rect width="32" height="32" rx="4" fill="var(--blue)"/><path d="M8 16l6 6 11-12" stroke="#fff" stroke-width="2.5" fill="none"/></svg><b>Pre-Production:</b> Concept development, scripting, and storyboarding tailored to your message.</li>
      <li><svg width="32" height="32" viewBox="0 0 32 32"><rect width="32" height="32" rx="4" fill="var(--blue)"/><path d="M8 16l6 6 11-12" stroke="#fff" stroke-width="2.5" fill="none"/></svg><b>Cinematic Production:</b> Director-led shoots with pro crews, 4K+ gear, and lighting that sets the mood.</li>
      <li><svg width="32" height="32" viewBox="0 0 32 32"><rect width="32" height="32" rx="4" fill="var(--blue)"/><path d="M8 16l6 6 11-12" stroke="#fff" stroke-width="2.5" fill="none"/></svg><b>Post-Production:</b> Editing, color grading, and sound design that polishes your story to perfection.</li>
    </ul>
  </section>

  <section>
    <div class="photo-band" role="img" aria-label="Ballroom with a projected event title screen and banquet tables" style="top:2595px;height:395px;background:linear-gradient(180deg,#1c2030 0%,#4c4858 35%,#3a3a3e 65%,#0c0c0f 100%)"></div>
    <h2 class="band-title display" style="top:2903px;font-size:74px;line-height:90px">SERVICES WE OFFER</h2>

    <article class="service-card" style="left:60px;top:3065px">
      <div class="thumb" role="img" aria-label="Speaker on stage in front of a blue-lit event screen" style="background:linear-gradient(160deg,#2a3aa8,#3c2e6e 60%,#1a1830)"></div>
      <h3>Event Production</h3>
      <p style="top:256px">We will help you bring your vision to life through our expert audio visual, planning, logistics, lighting, staging, and design services.</p>
    </article>
    <article class="service-card" style="left:427px;top:3065px">
      <div class="thumb" role="img" aria-label="Broadcast camera facing a podium with a logo backdrop" style="background:linear-gradient(160deg,#c9c4bc,#5c4a3a 55%,#1e1c1c)"></div>
      <h3>Film &amp; Videography</h3>
      <p style="top:256px">We work closely with our clients to understand their message and develop a customized approach to capturing and conveying it on screen.</p>
    </article>
    <article class="service-card" style="left:793px;top:3065px">
      <div class="thumb" role="img" aria-label="Presenter beside a wide video wall at a conference" style="background:linear-gradient(160deg,#3a5aa0,#22304e 55%,#151820)"></div>
      <h3>Meeting, Conference &amp; Gala Planning</h3>
      <p style="top:284px">We work with local and national clients, consulting on several aspects of the meeting, conference and gala planning process.</p>
    </article>
    <article class="service-card" style="left:243px;top:3430px">
      <div class="thumb" role="img" aria-label="Trade show booth with display screens and product stands" style="background:linear-gradient(160deg,#dfe6ee,#7badd7 50%,#3a5a7a)"></div>
      <h3>Hyrbid Event Design</h3>
      <p style="top:256px">Live and virtual services for a conference, trade show, or product launch, we have the expertise and experience to help you make it a success.</p>
    </article>
    <article class="service-card" style="left:610px;top:3430px">
      <div class="thumb" role="img" aria-label="Close view of a lit audio mixing console and monitors" style="background:linear-gradient(160deg,#4a4e5a,#23252c 55%,#121316)"></div>
      <h3>Audio Visual Production</h3>
      <p style="top:256px">We have over 20 years of expertise in Audio Visual contracting, staffing and equipment allocation and believe this is essential for your event's success.</p>
    </article>
  </section>

  <section>
    <svg class="abs" style="left:105px;top:3960px" width="58" height="46" viewBox="0 0 58 46"><path fill="var(--lavender)" d="M0 46V24C0 10 7 2 22 0v9c-7 2-10 6-10 13h10v24zM34 46V24C34 10 41 2 56 0v9c-7 2-10 6-10 13h10v24z"/></svg>
    <p class="quote-copy">I want to thank you and your team fordoing an excellent job with the set up for the red carpet award night. The stage looks amazing and your efforts makes the event memorable. We truly appreciate <b>your professionalism, quick turnaround and quality of work</b>...</p>
    <p class="abs" style="left:105px;top:4192px;font-size:16px;font-weight:700">JOB WELL DONE!!!</p>
    <p class="abs" style="left:105px;top:4252px;font-size:21px;letter-spacing:1px;color:#e6e6ea">- MERIDALE CONSULTING</p>
    <div class="photo" role="img" aria-label="Red carpet between gold stanchions in front of red stage curtains" style="left:673px;top:3930px;width:467px;height:390px;background:linear-gradient(180deg,#3a0608,#a01218 45%,#6a0a0e 75%,#1a0a0a)"></div>
  </section>

  <section class="cta">
    <h2 class="abs display" style="left:60px;top:62px;font-size:38px;line-height:46px">Ready to Captivate Your Audience—Anywhere?</h2>
    <p class="abs" style="left:60px;top:128px;font-size:16px;color:#e6e6ea">Let's discuss your next event, film project, or both.</p>
    <a class="btn" style="left:884px;top:67px;width:256px;height:46px">Request a Free Quote</a>
  </section>

  <footer class="site-footer">© 2025 Halvindor Stage Production. All rights reserved</footer>
</div>
</body>
</html>
```